Brightvane Group Word Press Website

We need a graphical, fun website that conveys our messaging of providing the Top-Tier Keystone Outreach Program for Mortgage Loan Officers and Realtors. Our system uses AI and Predictive Analysis to uncover the 'Gold' hidden in contact databases. The 'Gold' is defined as people who are in the market or likely to be in the market soon. We place that 'Gold' in the form of Contact Name, Address, Phone and Email on a Daily To Do List detailing what type of contact should be made.

Target Market(s)

Mortgage Loan Officers and Realtors

Industry/Entity Type

Mortgage & Real Estate

Coding

Coded - Design and coding required

Number of Pages Required

5+ page

Requirements
Must have
• I like the look of this site- https://www.hearthloanstudio.example/
Nice to have
• Please create a flow that is similar to https://www.hearthloanstudio.example/, but better, more dynamic. Site must be responsive and mobile friendly. Site will have embedded videos. Site need to convey a message of hope, imagination, innovation, results oriented, better than the rest, victory!
Should not have
• Nothing cheesy or low class.

```html
<!DOCTYPE html>
<html lang="en">
<head>
<meta charset="utf-8">
<title>Brightvane Group</title>
<link rel="stylesheet" href="https://fonts.googleapis.com/css2?family=Outfit:wght@300;400;500;600;700&display=swap">
<style>
:root{
  --navy:#1f2b4d;
  --blue-deep:#083d91;
  --blue:#0a4bb0;
  --yellow:#f4d04f;
  --orange:#f9b93a;
  --pale:#f5f9fb;
  --line:#e6ebf0;
  --muted:#6b7385;
  --white:#fff;
  --chart-a:#3b3fd6;
  --chart-b:#1cc7d6;
}
*{box-sizing:border-box;margin:0;padding:0}
html,body{width:1200px;height:2331px;overflow:hidden}
body{font-family:"Outfit",sans-serif;color:var(--navy);background:var(--white);position:relative}
.abs{position:absolute}

/* header */
.site-header{left:0;top:0;width:1200px;height:82px;background:var(--white)}
.brand{left:68px;top:28px;display:flex;align-items:center;gap:10px;font-size:19px;font-weight:600;color:var(--navy);letter-spacing:.5px}
.brand-dot{width:24px;height:24px;border-radius:50%;background:var(--yellow)}
.main-nav{left:679px;top:42px;display:flex;gap:42px;font-size:12px;font-weight:500;letter-spacing:.4px}
.nav-contact{left:991px;top:36px;width:77px;height:29px;border:1px solid var(--navy);font-size:9px;font-weight:500;letter-spacing:.6px;display:flex;align-items:center;justify-content:center}

/* hero */
.hero{left:0;top:82px;width:1200px;height:590px;background:linear-gradient(110deg,var(--blue-deep),var(--blue))}
.hero-title{left:170px;top:140px;color:var(--white);font-size:50px;font-weight:700;line-height:70px;letter-spacing:.5px}
.hero-sub{left:170px;top:278px;color:var(--white);font-size:38px;font-weight:300;letter-spacing:.5px}
.hero-tag{left:171px;top:339px;color:var(--white);font-size:15px;font-weight:500;letter-spacing:.6px}
.btn{background:var(--yellow);border-radius:20px;display:flex;align-items:center;justify-content:center;gap:8px;font-size:9px;font-weight:700;letter-spacing:.4px;color:var(--navy)}
.hero-btn{left:170px;top:381px;width:141px;height:38px;box-shadow:0 6px 14px rgba(0,0,0,.2)}
.hero-media{left:614px;top:123px;width:485px;height:325px;background:linear-gradient(120deg,#c9ccd0,#6f7378 55%,#3a3d42)}
.play{left:202px;top:122px;width:80px;height:80px;border-radius:50%;background:rgba(244,208,79,.85)}

/* services */
.section-title{width:1200px;left:0;text-align:center;font-size:32px;font-weight:600;letter-spacing:.5px;color:var(--navy)}
.services-grid{left:169px;top:831px;width:861px;height:302px;display:grid;grid-template-columns:repeat(3,1fr);grid-template-rows:151px 151px}
.service{position:relative;border:1px solid var(--line);background:var(--white)}
.service.tint{background:var(--pale);border-color:transparent}
.service-icon{position:absolute;left:35px;top:31px;width:36px;height:36px;border-radius:50%}
.service-icon.y{background:#f6e08c}
.service-icon.l{background:#eef0f7}
.service-name{position:absolute;left:35px;top:105px;font-size:13px;font-weight:500;color:var(--navy)}
.service-arrow{position:absolute;right:44px;top:108px}
.more-btn{left:530px;top:1192px;width:140px;height:38px}

/* about */
.about-band{left:0;top:1303px;width:1200px;height:563px;background:var(--pale)}
.about-text{left:385px;top:1408px;width:430px;text-align:center;font-size:12.5px;line-height:20px;color:var(--navy)}
.chart{left:312px;top:1478px}
.chart-labels{left:300px;top:1679px;width:590px;display:flex;justify-content:space-between;font-size:9px;color:var(--muted)}

/* contact */
.footer-band{left:0;top:2035px;width:1200px;height:296px;background:linear-gradient(110deg,var(--blue-deep),var(--blue))}
.contact-card{left:311px;top:1741px;width:588px;height:383px;background:var(--white);box-shadow:0 4px 20px rgba(20,40,80,.06)}
.contact-title{left:0;top:30px;width:100%;text-align:center;font-size:31px;font-weight:600;color:var(--navy)}
.contact-sub{left:0;top:83px;width:100%;text-align:center;font-size:11.5px;color:var(--muted)}
.field{border:1px solid var(--line);font-size:10px;color:var(--muted);padding:13px 13px}
.submit{left:237px;top:307px;width:113px;height:41px;background:var(--orange);border-radius:21px}

/* footer */
.footer-brand{left:258px;top:2259px;display:flex;align-items:center;gap:8px;color:var(--white);font-size:18px;font-weight:600;letter-spacing:.6px}
.footer-brand .brand-dot{width:18px;height:18px}
.footer-info{left:489px;top:2174px;color:var(--white)}
.info-row{position:relative;padding-left:22px}
.info-row svg{position:absolute;left:0;top:2px}
.info-head{font-size:10px;font-weight:600;letter-spacing:.4px}
.info-small{font-size:9.5px;line-height:14px;color:rgba(255,255,255,.7);margin-top:6px}
.info-phone{font-size:12.5px;font-weight:600;margin-top:14px}
.info-mail{font-size:10px;color:rgba(255,255,255,.7);margin-top:12px}
.footer-links{left:748px;top:2174px;display:flex;flex-direction:column;gap:9px;color:var(--white);font-size:10px}
.socials{left:900px;top:2212px;display:flex;gap:20px}
.socials span{width:8px;height:8px;border-radius:50%;background:var(--white)}
.copyright{left:890px;top:2241px;font-size:8px;color:rgba(255,255,255,.6)}
</style>
</head>
<body>

<header class="site-header abs">
  <div class="brand abs"><span class="brand-dot"></span>BRIGHTVANE GROUP</div>
  <nav class="main-nav abs"><span>Home</span><span>About</span><span>Services</span><span>Blog</span></nav>
  <div class="nav-contact abs">CONTACT</div>
</header>

<section class="hero abs">
  <h1 class="hero-title abs">FIND THE RIGHT<br>MORTGAGE</h1>
  <div class="hero-sub abs">OPTION FOR YOU!</div>
  <p class="hero-tag abs">Big Dreams Even Bigger And Better Loans.</p>
  <div class="btn hero-btn abs">GET STARTED</div>
  <div class="hero-media abs" role="img" aria-label="Video still: a man working at a desktop computer in a busy office">
    <div class="play abs"></div>
    <svg class="abs" style="left:233px;top:150px" width="22" height="26" viewBox="0 0 22 26"><path d="M2 1 L21 13 L2 25 Z" fill="#111"/></svg>
  </div>
</section>

<h2 class="section-title abs" style="top:752px">OUR SERVICES</h2>
<div class="services-grid abs">
  <div class="service"><span class="service-icon l"></span><span class="service-name">Brand Design &amp; Strategy</span><svg class="service-arrow" width="22" height="10" viewBox="0 0 22 10"><path d="M0 5H20M16 1L20 5L16 9" fill="none" stroke="#1f2b4d" stroke-width="1.3"/></svg></div>
  <div class="service tint"><span class="service-icon y"></span><span class="service-name">Social Media Management</span><svg class="service-arrow" width="22" height="10" viewBox="0 0 22 10"><path d="M0 5H20M16 1L20 5L16 9" fill="none" stroke="#1f2b4d" stroke-width="1.3"/></svg></div>
  <div class="service"><span class="service-icon l"></span><span class="service-name">Mortgage Chatbot</span><svg class="service-arrow" width="22" height="10" viewBox="0 0 22 10"><path d="M0 5H20M16 1L20 5L16 9" fill="none" stroke="#1f2b4d" stroke-width="1.3"/></svg></div>
  <div class="service tint"><span class="service-icon y"></span><span class="service-name" style="font-size:15px;left:40px">SEO</span><svg class="service-arrow" width="22" height="10" viewBox="0 0 22 10"><path d="M0 5H20M16 1L20 5L16 9" fill="none" stroke="#1f2b4d" stroke-width="1.3"/></svg></div>
  <div class="service"><span class="service-icon l"></span><span class="service-name" style="left:51px">Content Marketing</span><svg class="service-arrow" width="22" height="10" viewBox="0 0 22 10"><path d="M0 5H20M16 1L20 5L16 9" fill="none" stroke="#1f2b4d" stroke-width="1.3"/></svg></div>
  <div class="service tint"><span class="service-icon y"></span><span class="service-name">Reputation Management</span><svg class="service-arrow" width="22" height="10" viewBox="0 0 22 10"><path d="M0 5H20M16 1L20 5L16 9" fill="none" stroke="#1f2b4d" stroke-width="1.3"/></svg></div>
</div>
<div class="btn more-btn abs">VIEW MORE <svg width="14" height="8" viewBox="0 0 14 8"><path d="M0 4H12M9 1L12 4L9 7" fill="none" stroke="#1f2b4d" stroke-width="1.2"/></svg></div>

<section class="about-band abs"></section>
<h2 class="section-title abs" style="top:1358px">ABOUT US</h2>
<p class="about-text abs">Lorem ipsum dolor sit amet, consectetuer adipiscing elit, sed diam nonummy nibh euismod tincidunt ut laoreet dolore magna aliquam erat volutpat..</p>
<svg class="chart abs" width="567" height="192" viewBox="-5 -2 567 192">
  <g stroke="#e4e8ee" stroke-width="1">
    <path d="M0 0H557M0 31H557M0 62H557M0 92H557M0 123H557M0 154H557M0 185H557"/>
    <path d="M0 0V185M70 0V185M140 0V185M210 0V185M279 0V185M349 0V185M419 0V185M488 0V185M557 0V185"/>
  </g>
  <polyline fill="none" stroke="var(--chart-a)" stroke-width="1.5" points="0,73 70,33 140,62 210,52 279,61 349,42 419,52 488,42 557,34"/>
  <polyline fill="none" stroke="var(--chart-b)" stroke-width="1.5" points="0,108 70,100 140,124 210,101 279,123 349,118 419,92 488,106 557,62"/>
  <g fill="#fff" stroke="var(--chart-a)" stroke-width="1.3">
    <circle cx="0" cy="73" r="2.5"/><circle cx="70" cy="33" r="2.5"/><circle cx="140" cy="62" r="2.5"/><circle cx="210" cy="52" r="2.5"/><circle cx="279" cy="61" r="2.5"/><circle cx="349" cy="42" r="2.5"/><circle cx="419" cy="52" r="2.5"/><circle cx="488" cy="42" r="2.5"/><circle cx="557" cy="34" r="2.5"/>
  </g>
  <g fill="#fff" stroke="var(--chart-b)" stroke-width="1.3">
    <circle cx="0" cy="108" r="2.5"/><circle cx="70" cy="100" r="2.5"/><circle cx="140" cy="124" r="2.5"/><circle cx="210" cy="101" r="2.5"/><circle cx="279" cy="123" r="2.5"/><circle cx="349" cy="118" r="2.5"/><circle cx="419" cy="92" r="2.5"/><circle cx="488" cy="106" r="2.5"/><circle cx="557" cy="62" r="2.5"/>
  </g>
  <rect x="220" y="80" width="127" height="24" rx="2" fill="#fff"/>
  <text x="283" y="95.5" text-anchor="middle" font-family="Outfit, sans-serif" font-size="8.5" fill="#1f2b4d">line2 : $4,000 increasese</text>
</svg>
<div class="chart-labels abs"><span>1 Jan</span><span>1 Feb</span><span>1 Mar</span><span>1 Apr</span><span>1 May</span><span>1 Jun</span><span>1 Jul</span><span>1 Aug</span><span>1 Sep</span></div>

<footer class="footer-band abs"></footer>

<section class="contact-card abs">
  <h2 class="contact-title abs">Contact Us</h2>
  <p class="contact-sub abs">Let Make Something Together</p>
  <div class="field abs" style="left:106px;top:126px;width:181px;height:37px">Name</div>
  <div class="field abs" style="left:300px;top:126px;width:181px;height:37px">Email</div>
  <div class="field abs" style="left:106px;top:176px;width:181px;height:37px">Address</div>
  <div class="field abs" style="left:300px;top:176px;width:181px;height:37px">Phone</div>
  <div class="field abs" style="left:106px;top:226px;width:375px;height:66px">Message</div>
  <div class="btn submit abs">SUBMIT</div>
</section>

<div class="footer-brand abs"><span class="brand-dot"></span>BRIGHTVANE GROUP</div>
<div class="footer-info abs">
  <div class="info-row">
    <svg width="9" height="12" viewBox="0 0 9 12"><path d="M4.5 0C2 0 0 2 0 4.5C0 8 4.5 12 4.5 12S9 8 9 4.5C9 2 7 0 4.5 0Z" fill="#fff"/><circle cx="4.5" cy="4.5" r="1.6" fill="#0a4bb0"/></svg>
    <div class="info-head">BRIGHTVANE GROUP</div>
    <div class="info-small">Lorem ipsum udit dolor sit<br>amet adipiscing , 1230</div>
  </div>
  <div class="info-row info-phone">
    <svg width="10" height="10" viewBox="0 0 10 10" style="top:3px"><path d="M2 0L4 2.5L3 4C3.6 5.3 4.7 6.4 6 7L7.5 6L10 8L9 10C4 10 0 6 0 1Z" fill="#fff"/></svg>
    555-014-7720
  </div>
  <div class="info-row info-mail">
    <svg width="10" height="8" viewBox="0 0 10 8" style="top:3px"><rect width="10" height="8" fill="#fff"/><path d="M0 0L5 4L10 0" fill="none" stroke="#0a4bb0" stroke-width="1"/></svg>
    info@brightvanegroup.example
  </div>
</div>
<nav class="footer-links abs"><span>Home</span><span>About us</span><span>Services</span><span>Blog</span><span>Contact</span></nav>
<div class="socials abs"><span></span><span></span><span></span></div>
<div class="copyright abs">© 2022 Brightvane Group.</div>

</body>
</html>
```